high impact Wine label for retail market

We are a medium size winery that plans to re-enter the retail market so we need your help.the name of the wine in called "Torre Valmira".
it has to draw attention to make you pick it up after you open it the wine does his job being a quality wine.you can check out our website www.domeniulcorvesti.ro for detailes and pictures of our old labels.you can use elements of castle (recomanded) font of the text must be something specific of the midlle ages we will offer anny suport . impress us .we will have more projects.
p.s the label can be standard or it can any shape you consider pleasent.

good luck

Target Market(s)

men,women ,retail market

Industry/Entity Type

French Wine

Font styles to use
Other font styles liked:
• old,middle ages ,or anything at your convenience

Requirements
Must have
• must have a castle but if you have a design without a castle is ok submit it we are flexible.
Nice to have
• element of grape culture in background but not necesary at your discretion,castle,

```html
<!DOCTYPE html>
<html lang="en">
<head>
<meta charset="utf-8">
<title>Torre Valmira – Wine Label</title>
<link rel="stylesheet" href="https://fonts.googleapis.com/css2?family=UnifrakturCook:wght@700&family=Great+Vibes&family=IM+Fell+English&display=swap">
<style>
  :root {
    --backdrop: #1c1c1d;
    --paper: #efe6d2;
    --wine-red: #8c1c1f;
    --ink: #5e1013;
    --ink-soft: #7a2a2c;
  }
  html, body {
    margin: 0;
    padding: 0;
    width: 880px;
    height: 1200px;
    overflow: hidden;
    background: var(--backdrop);
  }
  .canvas {
    position: relative;
    width: 880px;
    height: 1200px;
  }
  .label {
    position: absolute;
    left: 120px;
    top: 170px;
    width: 640px;
    height: 860px;
  }
  .label-frame {
    position: absolute;
    inset: 0;
    width: 640px;
    height: 860px;
  }
  .label-text {
    position: absolute;
    inset: 0;
    display: flex;
    flex-direction: column;
    align-items: center;
    text-align: center;
    color: var(--ink);
  }
  .wine-name {
    margin: 72px 0 0;
    font-family: "UnifrakturCook", serif;
    font-weight: 700;
    font-size: 108px;
    line-height: 118px;
  }
  .divider {
    width: 420px;
    height: 2px;
    background: var(--wine-red);
    margin: 22px 0 16px;
  }
  .grape-variety {
    font-family: "Great Vibes", cursive;
    font-size: 70px;
    line-height: 80px;
  }
  .sweetness {
    font-family: "IM Fell English", serif;
    font-size: 36px;
    line-height: 42px;
    margin-top: 2px;
  }
  .region {
    font-family: "UnifrakturCook", serif;
    font-weight: 700;
    font-size: 92px;
    line-height: 104px;
    margin-top: 30px;
  }
  .appellation {
    font-family: "IM Fell English", serif;
    font-size: 32px;
    letter-spacing: 2px;
    margin-top: 4px;
  }
  .details {
    font-family: "IM Fell English", serif;
    font-size: 22px;
    line-height: 28px;
    color: var(--ink-soft);
    margin-top: 14px;
  }
</style>
</head>
<body>
<main class="canvas">
  <section class="label">
    <svg class="label-frame" viewBox="0 0 640 860" aria-hidden="true">
      <path fill="var(--paper)" d="M50,0 H590 A50 50 0 0 0 640 50 V810 A50 50 0 0 0 590 860 H50 A50 50 0 0 0 0 810 V50 A50 50 0 0 0 50 0Z"/>
      <path fill="var(--wine-red)" d="M60,10 H580 A50 50 0 0 0 630 60 V800 A50 50 0 0 0 580 850 H60 A50 50 0 0 0 10 800 V60 A50 50 0 0 0 60 10Z"/>
      <path fill="var(--paper)" d="M74,30 H566 A44 44 0 0 0 610 74 V786 A44 44 0 0 0 566 830 H74 A44 44 0 0 0 30 786 V74 A44 44 0 0 0 74 30Z"/>
      <path fill="none" stroke="var(--wine-red)" stroke-width="2" d="M80,40 H560 A40 40 0 0 0 600 80 V780 A40 40 0 0 0 560 820 H80 A40 40 0 0 0 40 780 V80 A40 40 0 0 0 80 40Z"/>
    </svg>
    <div class="label-text">
      <h1 class="wine-name">Torre<br>Valmira</h1>
      <div class="divider"></div>
      <p class="grape-variety" style="margin:0">Fetească Neagră</p>
      <p class="sweetness" style="margin:0">demisec</p>
      <p class="region" style="margin-bottom:0">Valdoria</p>
      <p class="appellation" style="margin:0">DOC-CT</p>
      <p class="details" style="margin-bottom:0">13,5% vol<br>750 ml</p>
    </div>
  </section>
</main>
</body>
</html>
```